Ward Compass Business Card Design*

We need a business card design for our company Ward Compass. Our company is specialized in providing online consulting services regarding medical institutions, hospitals and doctors. We work with patients worldwide looking to choose between healthcare providers. We have a website you may use as a reference, where we list doctors and clinics worldwide. So we target Medical providers as well as patients worldwide.
Target Market(s)
Medical Providers and patients around the world
Industry/Entity Type
Medical
Contact Information for Business Card
Salma Derkaoui
CEO
+90 612 348 2071
info@wardcompass-example.com
www.wardcompass-example.com
14 Annakhil 3 H.R.B. Rabat, Morocco
Requirements
Must have
- Company logo/name on one full side, personal info and smaller logo and company name on the other side.
Nice to have
- Smart and elegant design

```html
<!DOCTYPE html>
<html lang="en">
<head>
<meta charset="utf-8">
<title>Ward Compass – Business Card</title>
<link rel="stylesheet" href="https://fonts.googleapis.com/css2?family=Montserrat:wght@400;700&family=Lato:wght@400;700&display=swap">
<style>
  :root {
    --navy: #1b4778;
    --navy-deep: #0f2f5c;
    --ink: #1a2f5e;
    --grey-text: #4a4a4a;
    --paper: #f7f7f7;
    --backdrop: #2a2a2a;
  }
  * { margin: 0; padding: 0; box-sizing: border-box; }
  html, body {
    width: 1200px; height: 997px; overflow: hidden;
    background: var(--backdrop);
  }
  .stage { position: relative; width: 1200px; height: 997px; }

  /* Brand side */
  .card-front {
    position: absolute; left: 88px; top: 328px;
    width: 595px; height: 340px;
    background: linear-gradient(135deg, #22548a 0%, var(--navy) 55%, var(--navy-deep) 100%);
    display: flex; align-items: center; justify-content: center; gap: 22px;
    box-shadow: 0 10px 30px rgba(0,0,0,.45);
  }
  .brand-dot {
    width: 58px; height: 58px; border-radius: 50%;
    background: #ffffff;
  }
  .brand-name {
    font-family: "Montserrat", sans-serif; font-weight: 700;
    font-size: 40px; letter-spacing: 2px; color: #ffffff;
  }

  /* Info side */
  .card-back {
    position: absolute; left: 771px; top: 201px;
    width: 340px; height: 595px;
    background: var(--paper);
    overflow: hidden;
    box-shadow: 0 10px 30px rgba(0,0,0,.45);
  }
  .band-top { position: absolute; left: 0; top: 0; width: 100%; height: 22px; background: var(--navy); }
  .stripe { position: absolute; left: 0; width: 100%; background: var(--navy); }
  .band-bottom {
    position: absolute; left: 0; bottom: 0; width: 100%; height: 112px;
    background: var(--navy);
    display: flex; align-items: flex-start; justify-content: center; padding-top: 26px;
  }
  .tagline {
    font-family: "Lato", sans-serif; font-size: 14px; color: #ffffff; letter-spacing: .3px;
  }

  .logo-row {
    position: absolute; top: 86px; left: 0; width: 100%;
    display: flex; align-items: center; justify-content: center; gap: 10px;
  }
  .logo-dot { width: 30px; height: 30px; border-radius: 50%; background: var(--navy); }
  .logo-name {
    font-family: "Montserrat", sans-serif; font-weight: 700;
    font-size: 21px; letter-spacing: 1px; color: var(--ink);
  }

  .person { position: absolute; top: 186px; width: 100%; text-align: center; }
  .person-name {
    font-family: "Montserrat", sans-serif; font-weight: 700;
    font-size: 19px; color: var(--ink); letter-spacing: .5px;
  }
  .person-role {
    font-family: "Montserrat", sans-serif; font-weight: 700;
    font-size: 13px; color: var(--grey-text); margin-top: 2px;
  }

  .divider {
    position: absolute; left: 85px; width: 170px; height: 3px;
    background: linear-gradient(90deg, transparent, var(--ink) 50%, transparent);
  }

  .icon-row {
    position: absolute; width: 100%;
    display: flex; justify-content: center; gap: 16px;
  }
  .icon-row svg { width: 14px; height: 14px; fill: var(--ink); }

  .contact {
    position: absolute; top: 300px; width: 100%; text-align: center;
    font-family: "Lato", sans-serif; font-size: 15px; color: var(--grey-text); line-height: 21px;
  }
  .website {
    position: absolute; top: 408px; width: 100%; text-align: center;
    font-family: "Lato", sans-serif; font-weight: 700; font-size: 15px; color: var(--ink);
  }
</style>
</head>
<body>
<main class="stage">

  <section class="card-front" aria-label="Business card, brand side">
    <span class="brand-dot"></span>
    <span class="brand-name">WARD COMPASS</span>
  </section>

  <section class="card-back" aria-label="Business card, contact side">
    <div class="band-top"></div>
    <div class="stripe" style="top:28px;height:4px"></div>
    <div class="stripe" style="top:38px;height:3px"></div>

    <div class="logo-row">
      <span class="logo-dot"></span>
      <span class="logo-name">WARD COMPASS</span>
    </div>

    <div class="person">
      <p class="person-name">SALMA DERKAOUI</p>
      <p class="person-role">CEO</p>
    </div>

    <div class="divider" style="top:248px"></div>

    <div class="icon-row" style="top:276px">
      <svg viewBox="0 0 24 24" aria-label="Phone"><path d="M6.6 10.8a15.1 15.1 0 0 0 6.6 6.6l2.2-2.2c.3-.3.7-.4 1-.2 1.1.4 2.3.6 3.6.6.6 0 1 .4 1 1V20c0 .6-.4 1-1 1A17 17 0 0 1 3 4c0-.6.4-1 1-1h3.5c.6 0 1 .4 1 1 0 1.3.2 2.5.6 3.6.1.3 0 .7-.2 1z"/></svg>
      <svg viewBox="0 0 24 24" aria-label="Email"><path d="M2 5h20v14H2z M3.5 6.5 12 13l8.5-6.5" fill="none" stroke="#1a2f5e" stroke-width="2"/></svg>
    </div>

    <div class="contact">
      <p>+90 612 348 2071</p>
      <p>info@wardcompass-example.com</p>
    </div>

    <div class="divider" style="top:356px"></div>

    <div class="icon-row" style="top:384px">
      <svg viewBox="0 0 24 24" aria-label="Website"><circle cx="12" cy="12" r="9" fill="none" stroke="#1a2f5e" stroke-width="2"/><path d="M3 12h18M12 3c3 3 3 15 0 18M12 3c-3 3-3 15 0 18" fill="none" stroke="#1a2f5e" stroke-width="1.6"/></svg>
    </div>

    <p class="website">www.wardcompass-example.com</p>

    <div class="stripe" style="top:446px;height:4px"></div>
    <div class="stripe" style="top:456px;height:4px"></div>
    <div class="stripe" style="top:466px;height:4px"></div>

    <div class="band-bottom">
      <p class="tagline">Find &amp; compare top rated clinics world wide</p>
    </div>
  </section>

</main>
</body>
</html>
```